CorvanePharmacy brochure

Need a brochure design for an easy step guid about and how to order from CorvanePharmacy. We would like it very attractive but also clear to read as it is mainly targeting elderly. Attached is 2 alternate logos u can use and the information we would like the brochure to contain

```html
<!DOCTYPE html>
<html lang="en">
<head>
<meta charset="utf-8">
<title>CorvanePharmacy – Rural Medication Service Brochure</title>
<link href="https://fonts.googleapis.com/css2?family=Roboto:wght@300;400;500&display=swap" rel="stylesheet">
<style>
  :root {
    --brand-red: #c2122f;
    --paper: #ffffff;
    --ink: #3a3a3a;
    --stage: #f2f2f2;
    --panel-shadow: rgba(0, 0, 0, 0.12);
  }
  * { box-sizing: border-box; margin: 0; padding: 0; }
  html, body { width: 1200px; height: 900px; overflow: hidden; }
  body {
    background: var(--stage);
    font-family: "Roboto", Arial, sans-serif;
    color: var(--ink);
  }
  .brochure {
    position: absolute;
    left: 220px;
    top: 150px;
    width: 760px;
    height: 600px;
    display: flex;
    box-shadow: 0 10px 30px var(--panel-shadow);
  }
  .panel { width: 380px; height: 600px; position: relative; }

  /* Cover */
  .cover { background: var(--brand-red); color: var(--paper); }
  .brand {
    position: absolute;
    top: 42px;
    right: 34px;
    display: flex;
    align-items: center;
    gap: 10px;
  }
  .brand-dot {
    width: 30px; height: 30px;
    border: 2px solid var(--paper);
    border-radius: 50%;
  }
  .brand-text { display: flex; flex-direction: column; }
  .brand-name { font-weight: 500; font-size: 21px; letter-spacing: -0.3px; }
  .brand-tagline { font-weight: 300; font-size: 12px; margin-top: 2px; }
  .cover-title {
    position: absolute;
    left: 36px;
    bottom: 70px;
    font-weight: 300;
    font-size: 44px;
    line-height: 1.08;
    letter-spacing: -0.5px;
  }

  /* Inside panel */
  .inside { background: var(--paper); padding: 48px 40px; }
  .inside-heading {
    color: var(--brand-red);
    font-weight: 300;
    font-size: 46px;
    letter-spacing: -0.5px;
    margin-top: 28px;
  }
  .thermometer { position: absolute; top: 38px; right: 38px; }
  .service-list { list-style: none; margin-top: 150px; font-size: 17px; line-height: 1.55; }
  .service-list + .service-list { margin-top: 26px; }
  .call-line { margin-top: 36px; font-size: 17px; }
  .call-line .phone { color: var(--brand-red); font-weight: 500; }
</style>
</head>
<body>
  <div class="brochure">
    <section class="panel cover">
      <div class="brand">
        <span class="brand-dot"></span>
        <div class="brand-text">
          <span class="brand-name">CorvanePharmacy</span>
          <span class="brand-tagline">Local health you trust</span>
        </div>
      </div>
      <h1 class="cover-title">Rural<br>Medication<br>Service</h1>
    </section>

    <section class="panel inside">
      <h2 class="inside-heading">Need medicines?</h2>
      <svg class="thermometer" width="40" height="120" viewBox="0 0 40 120" aria-hidden="true">
        <rect x="10" y="2" width="20" height="88" rx="10" fill="var(--brand-red)"/>
        <circle cx="20" cy="98" r="18" fill="var(--brand-red)"/>
        <rect x="17" y="14" width="6" height="80" rx="3" fill="#fff"/>
        <circle cx="20" cy="98" r="9" fill="#fff"/>
        <g stroke="#fff" stroke-width="2">
          <line x1="24" y1="22" x2="30" y2="22"/>
          <line x1="24" y1="34" x2="30" y2="34"/>
          <line x1="24" y1="46" x2="30" y2="46"/>
          <line x1="24" y1="58" x2="30" y2="58"/>
          <line x1="24" y1="70" x2="30" y2="70"/>
        </g>
      </svg>
      <ul class="service-list">
        <li>Prescriptions accepted</li>
        <li>Tailored to your needs</li>
      </ul>
      <ul class="service-list">
        <li>Easy phone ordering</li>
        <li>Regular repeat supplying</li>
        <li>Health aids and vitamins</li>
      </ul>
      <p class="call-line">Call free <span class="phone">1 300 482 730</span></p>
    </section>
  </div>
</body>
</html>
```